Business Card Design for Kidvale (Hires out childrens play areas)

Looking to have a business card designed for a company we just bought. The company rents out childrens play areas.

I have uploaded a couple of examples of the kind of business card style I like. Here are two more examples:

https://quorvastudio.nz/project/bright-romp-branding/
https://imgvaultcdn.com/design_img/8841052/302917/302917_5518203_8841052_b73e19a2_image.jpg

I think a white card will be best due to all the colours in the logo.

Size we require: 3.75" x 2.25" (horizontally orientated) with a 0.125" bleed

Uploaded is two versions of our logo.

Details for the card:
1. My name: Liam Verster
2. Title: Managing Director
3. Phone no: 021 563 417
4. Email: liam@kidvale.co.nz
5. URL: www.kidvale.co.nz
6. Address:
PO Box 318625
Fernlea, Auckland

Let me know if you need anything else.

Target Market(s)

Hospitals, doctors surgeries, bed shops, etc.

Contact Information for Business Card

Details for the card:
1. My name: Liam Verster
3. Phone no: 021 563 417
5. URL: www.kidvale.co.nz
6. Address:
PO Box 318625
Fernlea, Auckland

Requirements
Should not have
• Not too busy.

```html
<!DOCTYPE html>
<html lang="en">
<head>
<meta charset="utf-8">
<title>Kidvale – Business Card</title>
<link rel="stylesheet" href="https://fonts.googleapis.com/css2?family=Source+Sans+3:wght@400;600&display=swap">
<style>
  :root {
    --page: #ffffff;
    --card: #dddcdc;
    --green: #3aaa49;
    --green-text: #2f9a44;
    --orange: #f7941d;
    --teal: #3a9a9a;
    --red: #ec2a2a;
    --purple: #7b2b8f;
    --blue: #2e3d98;
    --brand: #2e3d98;
  }
  * { margin: 0; padding: 0; box-sizing: border-box; }
  html, body {
    width: 1200px; height: 1200px; overflow: hidden;
    background: var(--page);
    font-family: "Source Sans 3", "Myriad Pro", sans-serif;
  }
  .canvas { position: relative; width: 1200px; height: 1200px; }

  .card {
    position: absolute; left: 184px; width: 756px; height: 454px;
    background: var(--card);
    box-shadow: 14px 14px 18px rgba(0,0,0,0.45);
  }
  .card--front { top: 88px; }
  .card--back { top: 632px; }

  .stripe { position: absolute; left: 0; width: 100%; height: 9px; }
  .stripe--green { top: 32px; background: var(--green); }
  .stripe--orange { top: 48px; background: var(--orange); }
  .stripe--teal { top: 397px; background: var(--teal); }
  .stripe--red { top: 413px; background: var(--red); }

  .brand-name {
    position: absolute; font-weight: 600; color: var(--brand);
    white-space: nowrap; transform: translate(-50%, -50%); line-height: 1;
  }
  .card--front .brand-name { left: 50%; top: 236px; font-size: 112px; }
  .card--back .brand-name { left: 200px; top: 224px; font-size: 74px; }

  .rule { position: absolute; width: 6px; }
  .rule--purple { left: 414px; top: 78px; height: 162px; background: var(--purple); }
  .rule--blue { left: 400px; top: 214px; height: 164px; background: var(--blue); }

  .person-name {
    position: absolute; left: 440px; top: 78px;
    font-size: 31px; color: var(--red); font-weight: 400; line-height: 1;
  }
  .person-title {
    position: absolute; left: 440px; top: 116px;
    font-size: 15px; color: var(--green-text); font-weight: 600;
  }

  .contact { position: absolute; left: 442px; display: flex; align-items: center; gap: 6px; font-size: 14.5px; }
  .contact svg { flex: none; }
  .contact--address { top: 168px; align-items: flex-start; color: var(--green-text); gap: 12px; line-height: 19px; }
  .contact--phone { top: 254px; color: var(--blue); }
  .contact--email { top: 301px; color: var(--red); }
  .contact--web { top: 338px; color: var(--red); }
</style>
</head>
<body>
<div class="canvas">

  <section class="card card--front">
    <div class="stripe stripe--green"></div>
    <div class="stripe stripe--orange"></div>
    <div class="brand-name">Kidvale</div>
    <div class="stripe stripe--teal"></div>
    <div class="stripe stripe--red"></div>
  </section>

  <section class="card card--back">
    <div class="stripe stripe--green"></div>
    <div class="stripe stripe--orange"></div>

    <div class="brand-name">Kidvale</div>

    <div class="rule rule--purple"></div>
    <div class="rule rule--blue"></div>

    <h1 class="person-name">Liam Verster</h1>
    <p class="person-title">Managing Director</p>

    <div class="contact contact--address">
      <svg width="20" height="30" viewBox="0 0 20 30" aria-hidden="true">
        <path d="M10 0C4.5 0 0 4.4 0 9.8 0 17 10 30 10 30S20 17 20 9.8C20 4.4 15.5 0 10 0z" fill="#2f9a44"/>
        <circle cx="10" cy="9.5" r="4" fill="#dddcdc"/>
      </svg>
      <address style="font-style:normal">PO Box 318625<br>Fernlea, Auckland</address>
    </div>

    <div class="contact contact--phone">
      <svg width="30" height="30" viewBox="0 0 30 30" aria-hidden="true">
        <circle cx="15" cy="15" r="13.5" fill="none" stroke="#2e3d98" stroke-width="2"/>
        <path d="M10.5 7.5l3 0.8-0.8 4-2 0.6c0.6 2.6 1.6 4.6 3.4 6.4l1.8-1 3 2.6-1.6 2.6c-5.5-0.8-9.5-7-8.4-13z" fill="#2e3d98"/>
      </svg>
      <span>021 563 417</span>
    </div>

    <div class="contact contact--email">
      <svg width="32" height="22" viewBox="0 0 32 22" aria-hidden="true">
        <rect x="0" y="0" width="32" height="22" fill="#ec2a2a"/>
        <path d="M1 1l15 11L31 1M1 21l11-10M31 21L20 11" fill="none" stroke="#dddcdc" stroke-width="1.8"/>
      </svg>
      <span>liam@kidvale.co.nz</span>
    </div>

    <div class="contact contact--web">
      <svg width="28" height="28" viewBox="0 0 28 28" aria-hidden="true">
        <circle cx="14" cy="14" r="13" fill="#ec2a2a"/>
        <path d="M1 14h26M14 1c-5 6-5 20 0 26M14 1c5 6 5 20 0 26M3 7h22M3 21h22" fill="none" stroke="#dddcdc" stroke-width="1.3"/>
      </svg>
      <span>www.kidvale.co.nz</span>
    </div>

    <div class="stripe stripe--teal"></div>
    <div class="stripe stripe--red"></div>
  </section>

</div>
</body>
</html>
```